Hadley & Partners, LLC Business Card 2016

We need a new business card design for a very important trade show coming up.

We are a compliance Consulting Firm. Our clients are stock brokerage firms and investment advisers.

I would like our logo on both sides of the card.

Info in the front of the card shold include:

Logo
First & Last Name
Title
Office #
Cell #
Email
Company Address (42 W. Calloway St., Suite 300 Pasadena, CA 91417

Back of the card should include the logo and url: www.hadleypartnersgroup.com

Target Market(s)

Stock Brokerage Firms and Investment Advisers

Industry/Entity Type

Financial Service

Contact Information for Business Card

Marcus J. Pellew
President
42 W. Calloway St., Suite 300
Pasadena, CA 91417
O 626.555.0147 ext. 204
C 818.555.0193
Email: marcus@hadleypartnersgroup.com
www.hadleypartnersgroup.com

Requirements
Nice to have
• The back of the card could be black with the logo with the white letters.
• I do want the front of the card to at least have the color logo with the black "Hadley & Partners Lettering.

```html
<!DOCTYPE html>
<html lang="en">
<head>
<meta charset="utf-8">
<title>Hadley &amp; Partners – Business Card</title>
<link href="https://fonts.googleapis.com/css2?family=Cinzel:wght@600&family=Montserrat:wght@400;700&family=Open+Sans:wght@400&display=swap" rel="stylesheet">
<style>
  :root{
    --backdrop:#d9d9d9;
    --paper:#ececec;
    --ink:#1b1b1b;
    --muted:#6a6a6a;
    --red:#c8261e;
    --black:#050505;
    --white:#ffffff;
  }
  *{margin:0;padding:0;box-sizing:border-box}
  html,body{width:1200px;height:900px;overflow:hidden}
  body{background:var(--backdrop);position:relative;font-family:"Open Sans",sans-serif}
  .card{position:absolute;left:320px;width:560px;height:320px;background:var(--paper);box-shadow:0 4px 14px rgba(0,0,0,.18);overflow:hidden}
  .card--back{top:100px}
  .card--front{top:470px;display:flex}

  .brand{display:flex;align-items:center;gap:16px}
  .brand__mark{width:42px;height:42px;background:var(--red);flex:none}
  .brand__name{font-family:"Cinzel",serif;font-weight:600;letter-spacing:.03em}

  .card--back .brand{position:absolute;left:56px;right:40px;top:86px}
  .card--back .brand__name{font-size:31px;color:var(--ink);white-space:nowrap}
  .card--back .band{position:absolute;left:0;right:0;top:212px;height:52px;background:var(--red)}

  .front__panel{width:218px;height:100%;background:var(--black);display:flex;align-items:center;justify-content:center;padding:0 16px}
  .front__panel .brand{flex-direction:column;gap:14px}
  .front__panel .brand__name{font-size:21px;line-height:1.15;color:var(--white);text-align:center;max-width:170px}
  .front__details{position:relative;flex:1;padding:44px 0 0 36px}
  .front__tab{position:absolute;top:-6px;right:20px;width:26px;height:40px;background:var(--red);border-radius:0 0 6px 6px}
  .person__name{font-family:"Montserrat",sans-serif;font-weight:700;font-size:19px;letter-spacing:.04em;color:var(--ink)}
  .person__title{font-family:"Montserrat",sans-serif;font-size:15px;letter-spacing:.04em;color:var(--muted);margin-top:2px}
  .person__rule{width:186px;height:2px;background:var(--red);margin:8px 0 22px}
  .contact{list-style:none}
  .contact__row{display:flex;align-items:center;gap:14px;margin-bottom:16px}
  .contact__icon{width:24px;height:24px;border-radius:5px;background:var(--red);flex:none;display:flex;align-items:center;justify-content:center}
  .contact__text{font-size:12.5px;line-height:1.35;color:var(--ink)}
</style>
</head>
<body>

<section class="card card--back" aria-label="Card back">
  <div class="brand">
    <span class="brand__mark"></span>
    <span class="brand__name">HADLEY &amp; PARTNERS</span>
  </div>
  <div class="band"></div>
</section>

<section class="card card--front" aria-label="Card front">
  <div class="front__panel">
    <div class="brand">
      <span class="brand__mark"></span>
      <span class="brand__name">HADLEY &amp;<br>PARTNERS</span>
    </div>
  </div>
  <div class="front__details">
    <span class="front__tab"></span>
    <p class="person__name">MARCUS J. PELLEW</p>
    <p class="person__title">PRESIDENT</p>
    <div class="person__rule"></div>
    <ul class="contact">
      <li class="contact__row">
        <span class="contact__icon">
          <svg width="14" height="14" viewBox="0 0 24 24" aria-hidden="true"><path fill="#fff" d="M6.6 10.8a15 15 0 0 0 6.6 6.6l2.2-2.2a1 1 0 0 1 1-.25 11.4 11.4 0 0 0 3.6.57 1 1 0 0 1 1 1V20a1 1 0 0 1-1 1A17 17 0 0 1 3 4a1 1 0 0 1 1-1h3.5a1 1 0 0 1 1 1c0 1.25.2 2.45.57 3.57a1 1 0 0 1-.25 1z"/></svg>
        </span>
        <p class="contact__text">O 626.555.0147 EXT. 204<br>C 818.555.0193</p>
      </li>
      <li class="contact__row">
        <span class="contact__icon">
          <svg width="14" height="14" viewBox="0 0 24 24" aria-hidden="true"><circle cx="12" cy="12" r="9" fill="none" stroke="#fff" stroke-width="2"/><path d="M3 12h18M12 3c3 3 3 15 0 18M12 3c-3 3-3 15 0 18" fill="none" stroke="#fff" stroke-width="1.6"/></svg>
        </span>
        <p class="contact__text">marcus@hadleypartnersgroup.com<br>www.hadleypartnersgroup.com</p>
      </li>
      <li class="contact__row">
        <span class="contact__icon">
          <svg width="14" height="14" viewBox="0 0 24 24" aria-hidden="true"><path fill="#fff" d="M12 3 2 12h3v8h5v-6h4v6h5v-8h3z"/></svg>
        </span>
        <p class="contact__text">42 W. Calloway St., Suite 300<br>Pasadena, CA 91417</p>
      </li>
    </ul>
  </div>
</section>

</body>
</html>
```